Bright Oak Consultant Services

I'm looking to create a flyer for my business to provide a consultant service. I will be providing the following below
Launch Your Business Today for only $150
(state fee not included)
Business Formation includes:
*Limited liability Corporation (LLC)
*Hale and Penwick Number
*FEIN
*Operation Agreement for partnership LLCs (For 2 or more member(s)
*Commercial Activity license (If needed for your Business )
*Same -day turnaround service with documents
Schedule your Appointment today
Call or text:413-902-6175
Email:MorvellCapitalCircle@quillpost.net
Target Market(s)
I want the flyer to attract people who wants to start a business but doesn’t know where to start. I want the flyer to stand out form the other consultant businesses.
Industry/Entity Type
Consultant
Requirements
Must have
- The State fee not included should be in small print
Highlight the price or service
Highlight the phrase "launch you business today"
Nice to have
- Different samples of colors, a variety
Should not have
- should not be all one color

```html
<!DOCTYPE html>
<html lang="en">
<head>
<meta charset="utf-8">
<title>Bright Oak Consultant Services – Launch Your Business Today</title>
<link rel="stylesheet" href="https://fonts.googleapis.com/css2?family=Poppins:wght@400;500;700&family=Oswald:wght@600;700&display=swap">
<style>
  :root {
    --page-bg: #e9e9ea;
    --brand-blue: #3d6db3;
    --blue-light: #5b8ad0;
    --brand-red: #e5394a;
    --red-deep: #c82333;
    --ink: #2b2b2b;
    --night: #0b0b0d;
    --paper: #ffffff;
  }
  * { box-sizing: border-box; margin: 0; padding: 0; }
  html, body { width: 1200px; height: 507px; overflow: hidden; }
  body {
    background: var(--page-bg);
    font-family: "Poppins", sans-serif;
    position: relative;
  }
  .flyer {
    position: absolute;
    left: 420px;
    top: 6px;
    width: 360px;
    height: 494px;
    background: var(--paper);
    overflow: hidden;
    box-shadow: 0 6px 18px rgba(0,0,0,.18);
  }
  .hero-band {
    position: absolute; left: 0; top: 0; width: 360px; height: 300px;
    background: linear-gradient(180deg, #3a67ae 0%, var(--brand-blue) 100%);
  }
  .hero-photo {
    position: absolute; left: 150px; top: 0; width: 190px; height: 300px;
    background: linear-gradient(180deg, #8fb0dc 0%, #cbd9ec 45%, #f4f6f9 100%);
  }
  .shapes { position: absolute; left: 0; top: 0; width: 360px; height: 494px; }
  .fee-note {
    position: absolute; left: 14px; top: 6px;
    color: var(--paper); font-size: 6px; font-weight: 400;
  }
  .fee-note::before { content: "• "; }
  .headline {
    position: absolute; left: 38px; top: 52px;
    color: var(--paper); font-size: 22px; font-weight: 700; line-height: 30px;
  }
  .services {
    position: absolute; left: 60px; top: 206px;
    list-style: none; color: var(--ink); font-size: 7.6px; line-height: 17px;
  }
  .services li { position: relative; padding-left: 0; }
  .services li::before {
    content: ""; position: absolute; left: -12px; top: 6px;
    width: 4px; height: 4px; border-radius: 50%; background: var(--ink);
  }
  .services li.note::before { display: none; }
  .services li.shift { margin-left: 3px; }
  .cta {
    position: absolute; left: 53px; top: 340px; width: 140px; height: 30px;
    border-radius: 15px; background: var(--brand-red);
    color: var(--paper); font-size: 7.2px; font-weight: 400;
    display: flex; align-items: center; justify-content: center;
  }
  .price-badge {
    position: absolute; left: 228px; top: 340px; width: 92px; height: 64px;
  }
  .price-badge .tag {
    position: absolute; left: 0; top: 6px; width: 92px; height: 52px;
    border-radius: 6px; background: var(--paper);
    border: 2px solid var(--night); overflow: hidden;
    box-shadow: 0 2px 4px rgba(0,0,0,.25);
  }
  .price-badge .amount {
    height: 38px; background: var(--brand-red); color: var(--paper);
    font-family: "Oswald", sans-serif; font-weight: 700; font-size: 28px;
    line-height: 38px; text-align: center;
  }
  .price-badge .only {
    height: 12px; background: var(--night); color: var(--paper);
    font-family: "Oswald", sans-serif; font-weight: 600; font-size: 6px;
    letter-spacing: 1.5px; line-height: 12px; text-align: center;
  }
  .contact {
    position: absolute; left: 68px; color: var(--paper);
    font-size: 7px; display: flex; align-items: center; gap: 10px;
  }
  .contact .icon {
    width: 9px; height: 9px; border-radius: 50%; background: var(--paper);
    display: flex; align-items: center; justify-content: center;
  }
  .contact.phone { top: 449px; }
  .contact.email { top: 464px; }
</style>
</head>
<body>
  <main class="flyer">
    <div class="hero-band"></div>
    <div class="hero-photo" role="img" aria-label="Photo of a professional in a white coat, arms crossed"></div>

    <svg class="shapes" viewBox="0 0 360 494" aria-hidden="true">
      <!-- fee tab -->
      <path d="M0,0 H135 C120,10 95,20 60,22 H0 Z" fill="var(--paper)"/>
      <path d="M0,0 H128 C114,9 92,17 58,18 H0 Z" fill="var(--brand-red)"/>
      <!-- red swoosh -->
      <path d="M0,186 C110,150 250,140 360,160 L360,330 C350,260 300,200 200,192 C120,188 60,195 0,205 Z" fill="var(--brand-red)"/>
      <path d="M0,196 C110,166 250,160 360,178 L360,300 C340,240 290,200 200,196 C120,192 60,198 0,210 Z" fill="var(--red-deep)" opacity=".35"/>
      <!-- white body -->
      <path d="M0,204 C80,189 190,184 260,194 C320,204 350,250 360,322 L360,494 L0,494 Z" fill="var(--paper)"/>
      <!-- footer waves -->
      <path d="M0,392 C110,360 250,380 360,420 L360,494 L0,494 Z" fill="var(--blue-light)"/>
      <path d="M0,404 C110,376 250,394 360,432 L360,494 L0,494 Z" fill="var(--brand-blue)"/>
      <path d="M0,420 C120,396 260,416 360,452 L360,494 L0,494 Z" fill="var(--night)"/>
      <!-- badge accents -->
      <g stroke="var(--ink)" stroke-width=".7">
        <line x1="246" y1="336" x2="282" y2="336"/>
        <line x1="256" y1="333" x2="274" y2="333"/>
        <line x1="308" y1="408" x2="322" y2="398"/>
        <line x1="312" y1="412" x2="326" y2="402"/>
      </g>
    </svg>

    <p class="fee-note">State fee not included</p>
    <h1 class="headline">Launch Your<br>Business<br>Today</h1>

    <ul class="services">
      <li>Limited liability Corporation (LLC)</li>
      <li>Hale and Penwick Number</li>
      <li>FEIN</li>
      <li>Operation Agreement for partnership LLCs</li>
      <li class="note">(For 2 or more member(s)</li>
      <li class="shift">Commercial Activity license (If needed for your Business )</li>
      <li class="shift">Same -day turnaround service with documents</li>
    </ul>

    <div class="cta">Schedule your Appointment today</div>

    <div class="price-badge">
      <div class="tag">
        <div class="amount">$150</div>
        <div class="only">ONLY</div>
      </div>
    </div>

    <p class="contact phone">
      <span class="icon"><svg width="6" height="6" viewBox="0 0 24 24"><path d="M6.6 10.8a15 15 0 0 0 6.6 6.6l2.2-2.2a1 1 0 0 1 1-.25 11.4 11.4 0 0 0 3.6.57 1 1 0 0 1 1 1V20a1 1 0 0 1-1 1A17 17 0 0 1 3 4a1 1 0 0 1 1-1h3.5a1 1 0 0 1 1 1c0 1.25.2 2.45.57 3.6a1 1 0 0 1-.25 1z" fill="#0b0b0d"/></svg></span>
      413-902-6175
    </p>
    <p class="contact email">
      <span class="icon"><svg width="6" height="6" viewBox="0 0 24 24"><rect x="2" y="5" width="20" height="14" rx="2" fill="#0b0b0d"/><path d="M3 6l9 7 9-7" stroke="#fff" stroke-width="2" fill="none"/></svg></span>
      MorvellCapitalCircle@quillpost.net
    </p>
  </main>
</body>
</html>
```